Mobile Fitness snd Therapy Business Card Design

I need a business card designed for my mobile fitness and therapy business.

Please view the images that I have uploaded. I like the simplicity of the design that I have attached. I adapted it with my information

Target Market(s)

Those seeking personal training, injury rehabilitation or massage therapy.

Industry/Entity Type

Business

Contact Information for Business Card

Dylan Marwick - MSc, CAT(C), RMT, CSCS, Pn2
e-mail: dylan@vantrelo.com
website: www.vantrelo.com
instagram: @dylan_marwick

Font styles to use
Sans Serif

Colors
3176b5
0355a3

Requirements
Must have
• "Contact us to receive a FREE assessment"
• Services offered:
• Personal Training
• Golf Fitness
• Injury Rehab
• Massage Therapy
• Yoga
Nice to have
• Consistent colours with brand
• - Dark Blue: #232837
• - Blue: #5096f0
• Consistent look/feel with the website: www.vantrelo.com

```html
<!DOCTYPE html>
<html lang="en">
<head>
<meta charset="utf-8">
<title>Vantrelo Business Card</title>
<link href="https://fonts.googleapis.com/css2?family=Roboto:wght@400;500;700;900&family=Roboto+Condensed:wght@500;700&display=swap" rel="stylesheet">
<style>
  :root {
    --navy: #232837;
    --blue: #2d5bd7;
    --blue-light: #5096f0;
    --paper: #f3f3f3;
    --ink: #444a55;
    --bg: #dcd9d4;
    --white: #ffffff;
  }
  * { margin: 0; padding: 0; box-sizing: border-box; }
  html, body { width: 1200px; height: 960px; overflow: hidden; }
  body {
    position: relative;
    background: var(--bg);
    font-family: "Roboto", Arial, sans-serif;
  }
  .card {
    position: absolute;
    width: 598px;
    height: 343px;
    border-radius: 22px;
    overflow: hidden;
    box-shadow: 0 3px 8px rgba(0,0,0,0.35);
  }
  /* Front */
  .card-front { left: 315px; top: 113px; background: var(--paper); }
  .brand {
    position: absolute;
    text-align: center;
    font-family: "Roboto", Arial, sans-serif;
  }
  .brand-name {
    display: block;
    font-weight: 700;
    line-height: 1;
    white-space: nowrap;
  }
  .brand-tagline {
    display: block;
    font-weight: 700;
    line-height: 1;
    white-space: nowrap;
  }
  .card-front .brand { left: 50px; top: 134px; width: 270px; color: var(--navy); }
  .card-front .brand-name { font-size: 35px; letter-spacing: 6px; margin-right: -6px; }
  .card-front .brand-tagline { font-size: 10.5px; letter-spacing: 2.5px; margin-top: 8px; margin-right: -2.5px; }
  .divider {
    position: absolute;
    left: 330px; top: 102px;
    width: 1px; height: 113px;
    background: linear-gradient(to bottom, transparent, #9a9da3 20%, #9a9da3 80%, transparent);
  }
  .person { position: absolute; left: 358px; top: 108px; }
  .person-name {
    font-family: "Roboto Condensed", Arial, sans-serif;
    font-weight: 700;
    font-size: 22px;
    color: var(--blue);
    line-height: 1;
  }
  .person-credentials {
    font-family: "Roboto Condensed", Arial, sans-serif;
    font-weight: 700;
    font-size: 10px;
    color: var(--blue);
    margin-top: 6px;
  }
  .contact-list { list-style: none; margin-top: 18px; }
  .contact-item {
    display: flex; align-items: center;
    font-size: 14px; color: var(--ink);
    height: 19px;
  }
  .contact-item svg { width: 14px; height: 14px; margin-right: 8px; flex: none; }
  .footer-band {
    position: absolute; left: 0; top: 296px;
    width: 100%; height: 28px;
    background: var(--navy);
  }
  .footer-accent {
    position: absolute; left: 0; top: 0;
    width: 84px; height: 28px;
    background: var(--blue);
  }
  .footer-web {
    position: absolute; left: 214px; top: 0;
    line-height: 28px;
    font-size: 14px;
    letter-spacing: 7px;
    color: var(--white);
  }
  /* Back */
  .card-back { left: 312px; top: 472px; background: var(--navy); }
  .card-back .brand { left: 0; top: 128px; width: 100%; color: var(--white); }
  .card-back .brand-name { font-size: 50px; letter-spacing: 9px; margin-right: -9px; }
  .card-back .brand-tagline { font-size: 16px; letter-spacing: 3.4px; margin-top: 9px; margin-right: -3.4px; }
  .cta {
    position: absolute; left: 58px; top: 259px;
    width: 482px; height: 32px;
    border-radius: 16px;
    background: var(--blue);
    color: var(--white);
    font-family: "Roboto", Arial, sans-serif;
    font-weight: 500;
    font-size: 19.5px;
    text-align: center;
    line-height: 32px;
    white-space: nowrap;
  }
  .services {
    position: absolute; left: 0; top: 297px; width: 100%;
    text-align: center;
    color: var(--white);
    font-size: 15px;
    white-space: nowrap;
  }
  .services .sep { color: #6b7590; margin: 0 4px; }
</style>
</head>
<body>

<section class="card card-front">
  <div class="brand">
    <span class="brand-name">VANTRELO</span>
    <span class="brand-tagline">NUTRITION - FITNESS - HEALTH</span>
  </div>
  <div class="divider"></div>
  <div class="person">
    <h1 class="person-name">DYLAN MARWICK</h1>
    <p class="person-credentials">MSC, CAT(C), RMT, CSCS, PN2</p>
    <ul class="contact-list">
      <li class="contact-item">
        <svg viewBox="0 0 14 14" aria-hidden="true"><rect x="1" y="3" width="12" height="8.5" rx="1" fill="#2d5bd7"/><path d="M1.5 3.8 L7 8 L12.5 3.8" fill="none" stroke="#fff" stroke-width="1.2"/></svg>
        dylan@vantrelo.com
      </li>
      <li class="contact-item">
        <svg viewBox="0 0 14 14" aria-hidden="true"><circle cx="7" cy="7" r="6.5" fill="#2d5bd7"/></svg>
        @dylan_marwick
      </li>
    </ul>
  </div>
  <div class="footer-band">
    <div class="footer-accent"></div>
    <span class="footer-web">www.vantrelo.com</span>
  </div>
</section>

<section class="card card-back">
  <div class="brand">
    <span class="brand-name">VANTRELO</span>
    <span class="brand-tagline">NUTRITION - FITNESS - HEALTH</span>
  </div>
  <p class="cta">CONTACT US TO RECEIVE A FREE ASSESSMENT</p>
  <p class="services">Personal Training<span class="sep">|</span>Golf Fitness<span class="sep">|</span>Injury Rehab<span class="sep">|</span>Massage Therapy<span class="sep">|</span>Yoga</p>
</section>

</body>
</html>
```